Vexel Business Cards

We need a new look business cvard to refelect our new look website www.vexel-example.com.au
We’re Vexel, a team of town planning and traffic and transport engineering specialists located in Melbourne.

Vexel is a company that is structured, articulate, dynamic, progressive, accurate and adaptable.
Our key messages are:
1. We make your life easier by doing what we do best
2. We tell you what you need to know not what you want to hear
3. Polished and professional but not afraid to show some personality

we would like a bold new look that is polished and professional but not afraid to show a bit of personality

Target Market(s)

Vexel’s diverse client base consists of architecture practices, builders, developers, local government and the legal fraternity.

Industry/Entity Type

Town

Requirements
Must have
• must use our logo and have the following information

Joel Harcastle
Director

Vexel Consultants Pty Ltd
Fernhollow Level 2
Tamber Street
Westmere VIC 3999 Australia
+61 03 9555 0187
mail@vexel-example.com.au
www.vexel-example.com.au
Nice to have
• We would like to see the logo used or the colours of the logo used.

```html
<!DOCTYPE html>
<html lang="en">
<head>
<meta charset="utf-8">
<title>Vexel Business Cards</title>
<link href="https://fonts.googleapis.com/css2?family=Roboto:wght@300;400;700&display=swap" rel="stylesheet">
<style>
  :root {
    --slate: #677f8b;
    --blue: #22a2e6;
    --light: #ececec;
    --divider: #d4d6d8;
    --ink: #3c4a52;
    --white: #ffffff;
    --page: #e4e5e6;
  }
  * { box-sizing: border-box; margin: 0; padding: 0; }
  html, body { width: 1200px; height: 1000px; overflow: hidden; }
  body {
    background: var(--page);
    font-family: "Roboto", Arial, sans-serif;
    position: relative;
  }
  .card {
    position: absolute;
    width: 700px;
    height: 400px;
    overflow: hidden;
    box-shadow: 0 6px 18px rgba(0,0,0,.18);
  }
  .card--front { left: 90px; top: 70px; background: var(--light); }
  .card--back { left: 410px; top: 530px; background: var(--slate); }

  /* front */
  .brand-panel {
    position: absolute; left: 0; top: 0; width: 330px; height: 270px;
    background: var(--slate);
  }
  .brand-panel .wordmark {
    position: absolute; left: 34px; bottom: 40px;
    font-weight: 300; font-size: 118px; line-height: 1; color: var(--white);
    letter-spacing: -2px;
  }
  .company {
    position: absolute; left: 0; top: 270px; width: 330px; height: 130px;
    padding: 22px 24px 0 28px;
    border-right: 4px solid var(--divider);
  }
  .company__name {
    font-weight: 700; font-size: 16px; color: var(--slate);
    text-transform: uppercase; letter-spacing: .3px;
    padding-bottom: 12px; border-bottom: 3px solid var(--divider);
  }
  .company__address {
    margin-top: 12px; font-size: 13px; line-height: 1.45; color: var(--ink);
  }
  .portrait {
    position: absolute; left: 330px; top: 0; width: 190px; height: 185px;
    background: linear-gradient(135deg, #f2f2f2 0%, #c9c9c9 55%, #8a8a8a 100%);
  }
  .name-band {
    position: absolute; left: 520px; top: 0; width: 180px; height: 185px;
    background: var(--blue); color: var(--white);
    padding: 0 18px 26px; display: flex; flex-direction: column; justify-content: flex-end;
  }
  .name-band svg { position: absolute; left: -12px; top: 120px; }
  .name-band__name { font-weight: 300; font-size: 22px; }
  .name-band__role { font-weight: 700; font-size: 14px; margin-top: 4px; }
  .contact {
    position: absolute; left: 334px; top: 185px; width: 366px; height: 140px;
    padding: 34px 28px; font-size: 13px; color: var(--ink); line-height: 1.7;
  }
  .contact dl { display: grid; grid-template-columns: 54px auto; }
  .web-band {
    position: absolute; left: 334px; top: 325px; width: 366px; height: 75px;
    background: var(--slate); color: var(--white);
    font-weight: 700; font-size: 16px;
    display: flex; align-items: center; justify-content: flex-end; padding-right: 28px;
  }

  /* back */
  .card--back .wordmark {
    position: absolute; left: 250px; top: 120px;
    font-weight: 300; font-size: 150px; line-height: 1; color: var(--white);
    letter-spacing: -3px;
  }
  .card--back .web {
    position: absolute; left: 110px; top: 300px;
    font-weight: 300; font-size: 17px; color: var(--white);
  }
</style>
</head>
<body>
  <section class="card card--front" aria-label="Business card front">
    <div class="brand-panel"><span class="wordmark">vexel</span></div>
    <div class="company">
      <p class="company__name">Vexel Consultants Pty Ltd</p>
      <p class="company__address">Add: 'Fernhollow' Level 2, 48 Tamber Street,<br>Westmere, Calder 3999, Australia.</p>
    </div>
    <div class="portrait" role="img" aria-label="Black and white portrait photo of the director"></div>
    <div class="name-band">
      <svg width="14" height="24" viewBox="0 0 14 24" aria-hidden="true"><polygon points="14,0 0,12 14,24" fill="#22a2e6"/></svg>
      <p class="name-band__name">Joel Harcastle</p>
      <p class="name-band__role">Director</p>
    </div>
    <div class="contact">
      <dl>
        <dt>Tel:</dt><dd>+61 03 9555 0187</dd>
        <dt>Email:</dt><dd>mail@vexel-example.com.au</dd>
      </dl>
    </div>
    <div class="web-band">www.vexel-example.com.au</div>
  </section>

  <section class="card card--back" aria-label="Business card back">
    <span class="wordmark">vexel</span>
    <span class="web">www.vexel-example.com.au</span>
  </section>
</body>
</html>
```